"Beyond Marrow Cay" Fictional Book Cover

BEYOND MARROW CAY
By: Dale Pruitt

Here's the intro .

"It had been nearly forty years since Ted Larraby last went to the island from where he was raised. Three months earlier he never would have thought about ever coming back. But life is weird. Things happen quickly and plans change, especially when your very life is at stake. The reason he was going back wasn’t to see old friends...no, no, no. They’re all dead. Of all the kids he grew up with on the island who moved off, he’s the only one still alive. Why?"

Pretty much all just a Lumeno book, by the way.

Target Market(s)

fiction readers

Requirements
Must have
• Somewhat of a dark, mysterious cover is what I'd like to see. Use your imagination. I've never written a fiction book before so I'm very open to ideas

Needs to have my name, DALE PRUITT at the bottom. like my other books, all of which are non-fiction
Nice to have
• Mysterious is what I'm looking for. NOT A HORROR story though. More a guy who left the island years ago, but is being called back to escape the rat race of modern, consumerist culture.

Please remember this NEEDS to jump out as a thumbnail on Bookvale as people are browsing. Mainly the WORDS need to stick out. Lighter words on a say a blue background.

If you want to try to use the attached pic, or something like this, to reflect an island in the cover, that'd be good.

I've also uploaded a couple images I purchased from Pixelcrate, hopefully you can make something work with these.

```html
<!DOCTYPE html>
<html lang="en">
<head>
<meta charset="utf-8">
<title>Beyond Marrow Cay – Book Cover</title>
<link rel="stylesheet" href="https://fonts.googleapis.com/css2?family=Oswald:wght@600&family=Big+Shoulders+Display:wght@700;900&family=Montserrat:wght@700&display=swap">
<style>
  :root {
    --backdrop: #3b332b;
    --paper: #dddcd8;
    --paper-light: #e7e6e2;
    --title-red: #9b3b24;
    --title-grey: #5e5e5e;
    --title-ink: #232323;
    --author-white: #f2f2f0;
    --mist: #b9b7b3;
    --shore-rust: #7d4f3c;
    --rock-grey: #6e6b68;
    --rock-dark: #464544;
    --sea-dark: #2a2a2a;
    --sea-deep: #1e1e1e;
  }
  * { margin: 0; padding: 0; box-sizing: border-box; }
  html, body {
    width: 1200px;
    height: 901px;
    overflow: hidden;
    background: var(--backdrop);
  }
  .cover {
    position: absolute;
    left: 335px;
    top: 28px;
    width: 530px;
    height: 845px;
    overflow: hidden;
    background: linear-gradient(180deg, var(--paper-light) 0%, var(--paper) 55%);
  }
  .cover-photo {
    position: absolute;
    left: 0;
    right: 0;
    top: 440px;
    bottom: 0;
    z-index: 0;
    background: linear-gradient(180deg,
      rgba(221,220,216,0) 0%,
      var(--mist) 9%,
      var(--rock-grey) 17%,
      var(--shore-rust) 24%,
      var(--shore-rust) 34%,
      var(--rock-grey) 44%,
      var(--rock-dark) 62%,
      var(--sea-dark) 80%,
      var(--sea-deep) 100%);
  }
  .title-block { position: relative; z-index: 1; }
  .title {
    position: absolute;
    left: 0;
    right: 0;
    text-align: center;
    line-height: 1;
  }
  .title-lead {
    top: 132px;
    font-family: "Oswald", sans-serif;
    font-weight: 600;
    font-size: 38px;
    letter-spacing: 0.2em;
    padding-left: 0.2em;
    color: var(--title-red);
  }
  .title-middle {
    top: 190px;
    font-family: "Big Shoulders Display", sans-serif;
    font-weight: 700;
    font-size: 96px;
    letter-spacing: 0.32em;
    padding-left: 0.32em;
    color: var(--title-grey);
  }
  .title-main {
    top: 280px;
    font-family: "Big Shoulders Display", sans-serif;
    font-weight: 900;
    font-size: 300px;
    letter-spacing: 0.04em;
    padding-left: 0.04em;
    color: var(--title-ink);
  }
  .author {
    position: absolute;
    z-index: 1;
    left: 0;
    right: 0;
    top: 773px;
    text-align: center;
    font-family: "Montserrat", sans-serif;
    font-weight: 700;
    font-size: 24px;
    color: var(--author-white);
  }
</style>
</head>
<body>
  <main class="cover">
    <div class="cover-photo" role="img" aria-label="Rocky island shoreline with red wooden houses above a grey sea"></div>
    <h1 class="title-block">
      <span class="title title-lead">BEYOND</span>
      <span class="title title-middle">MARROW</span>
      <span class="title title-main">CAY</span>
    </h1>
    <p class="author">By: Dale Pruitt</p>
  </main>
</body>
</html>
```